Email Signature Block Design for Law Firm

I would like you to create a similar signature block for my law firm . I saw the email signature block attached as image002.png and wanted a similar design for my law firm. I want to be able to swap the portraits for each of my staff from the final design. Our law firm colors are black, gold, white, red.

Law

• i like the red circle in around the photo in the oak ridge guild design. The Tall Cedar Guild desgn is what inspired me to have a signature block design for my firm.

```html
<!DOCTYPE html>
<html lang="en">
<head>
<meta charset="utf-8">
<title>Email Signature Block – The Harlow Firm</title>
<link rel="stylesheet" href="https://fonts.googleapis.com/css2?family=Oswald:wght@400;500&display=swap">
<style>
  :root {
    --paper: #ffffff;
    --ink: #000000;
    --logo-panel: #08090b;
    --red: #d62029;
    --gold: #e0a02a;
    --white: #ffffff;
  }
  html, body {
    margin: 0;
    width: 1200px;
    height: 1200px;
    overflow: hidden;
    background: var(--paper);
  }
  .canvas {
    position: relative;
    width: 1200px;
    height: 1200px;
    font-family: "Oswald", sans-serif;
  }
  .signature {
    position: absolute;
    left: 118px;
    top: 439px;
    width: 963px;
    height: 321px;
    box-sizing: border-box;
    border: 1px solid var(--ink);
    background: var(--paper);
    overflow: hidden;
  }
  .footer-band {
    position: absolute;
    left: 0;
    right: 0;
    bottom: 0;
    height: 95px;
    background: var(--ink);
  }
  .firm-panel {
    position: absolute;
    left: 23px;
    top: 232px;
    width: 341px;
    height: 81px;
    background: var(--logo-panel);
    display: flex;
    align-items: center;
    gap: 14px;
    padding-left: 20px;
    box-sizing: border-box;
  }
  .firm-mark {
    width: 14px;
    height: 14px;
    background: var(--gold);
  }
  .firm-name {
    color: var(--white);
    font-weight: 400;
    font-size: 24px;
    letter-spacing: 1px;
  }
  .identity {
    position: absolute;
    left: 81px;
    top: 106px;
    color: var(--ink);
  }
  .identity-name {
    margin: 0;
    font-size: 28px;
    font-weight: 500;
    line-height: 1.1;
    letter-spacing: 1px;
    transform: scaleX(0.9);
    transform-origin: left;
  }
  .identity-role {
    margin: 2px 0 0;
    font-size: 13px;
    font-weight: 400;
    letter-spacing: 1px;
  }
  .portrait-ring {
    position: absolute;
    left: 344px;
    top: 20px;
    width: 272px;
    height: 272px;
  }
  .contacts {
    position: absolute;
    left: 708px;
    top: 85px;
    margin: 0;
    padding: 0;
    list-style: none;
    color: var(--ink);
  }
  .contacts li {
    display: flex;
    align-items: center;
    gap: 9px;
    height: 21px;
    font-size: 14px;
    letter-spacing: 0.6px;
  }
  .contacts svg {
    width: 14px;
    height: 14px;
    flex: none;
  }
  .cta-bar {
    position: absolute;
    left: 689px;
    top: 256px;
    width: 172px;
    height: 35px;
    background: var(--red);
  }
</style>
</head>
<body>
<div class="canvas">
  <section class="signature">
    <div class="footer-band"></div>

    <div class="firm-panel">
      <span class="firm-mark"></span>
      <span class="firm-name">The Harlow Firm, PLLC</span>
    </div>

    <div class="identity">
      <h1 class="identity-name">YOUR NAME</h1>
      <p class="identity-role">Business Consultant</p>
    </div>

    <svg class="portrait-ring" viewBox="0 0 272 272" role="img" aria-label="Staff portrait photo framed by a red ring">
      <circle cx="136" cy="136" r="126" fill="#ffffff"/>
      <circle cx="136" cy="136" r="126" fill="none" stroke="#d62029" stroke-width="19.5"/>
    </svg>

    <ul class="contacts">
      <li>
        <svg viewBox="0 0 14 14" aria-hidden="true">
          <circle cx="7" cy="7" r="7" fill="#000"/>
          <path d="M4.6 3.6c.4-.3.8-.2 1 .2l.6 1.2c.1.3 0 .6-.2.8l-.4.3c.3.8 1 1.6 1.9 2l.4-.4c.2-.2.5-.3.8-.2l1.2.6c.4.2.5.6.2 1l-.5.6c-.4.4-1 .5-1.6.2C6 9.2 4.8 8 4.1 6.3c-.3-.6-.1-1.2.2-1.6z" fill="#fff"/>
        </svg>
        555-203-0148
      </li>
      <li>
        <svg viewBox="0 0 14 14" aria-hidden="true">
          <circle cx="7" cy="7" r="7" fill="#000"/>
          <rect x="3.6" y="4.6" width="6.8" height="4.8" rx="0.6" fill="#fff"/>
          <path d="M3.8 5l3.2 2.4L10.2 5" fill="none" stroke="#000" stroke-width="0.8"/>
        </svg>
        mara@oakridgeguild.com
      </li>
      <li>
        <svg viewBox="0 0 14 14" aria-hidden="true">
          <circle cx="7" cy="7" r="7" fill="#000"/>
          <circle cx="7" cy="7" r="3" fill="none" stroke="#fff" stroke-width="1.1"/>
        </svg>
        oakridgeguild.com
      </li>
    </ul>

    <div class="cta-bar"></div>
  </section>
</div>
</body>
</html>
```